Harborline Bridal Bakery Selling Method needs finishing touches to website.

We have a temporary website located at http://www.brivantomarketworks.com/ql/.
We are doing a responsive design and have created the architecture (layout). However, we need a professional makeover for the graphic elements and colors of the website. The website will be selling a sales course to mostly women who sell wedding cakes.
The photos within the posted website are for illustrative purposes. We will use our own photos after the website is redone.
We are open to changing the font styles, borders, header, and anything else as long as the layout is not changed.
Target Market(s)
75% women age 25-50 and men 30-60.
Industry/Entity Type
Architecture
Colors
Designer to choose colors to be used in the design.
Look and feel
Each slider illustrates characteristics of the customer's brand and the style your logo design should communicate.

```html
<!DOCTYPE html>
<html lang="en">
<head>
<meta charset="utf-8">
<title>Harborline Bridal Bakery Selling Method</title>
<link href="https://fonts.googleapis.com/css2?family=Carlito:wght@400;700&display=swap" rel="stylesheet">
<style>
:root{
  --page:#eeebe2;
  --white:#ffffff;
  --crimson:#c5264f;
  --crimson-dark:#9b1c3c;
  --sky:#0aa6e6;
  --sky-dark:#0a8fcf;
  --ink:#2b2b2b;
  --body:#444444;
  --muted:#8a8a8a;
  --card:#f3f3f3;
}
*{box-sizing:border-box;margin:0;padding:0}
html,body{width:1118px;height:1200px;overflow:hidden}
body{background:var(--page);font-family:"Carlito",sans-serif;color:var(--ink);position:relative}
.sheet{position:absolute;left:94px;top:0;width:928px;height:1112px;background:var(--white);box-shadow:0 1px 3px rgba(0,0,0,.15)}
.abs{position:absolute}
.tagline{left:124px;top:14px;font-size:21px;line-height:28px;color:var(--ink)}
.tagline strong{color:var(--sky-dark)}
.help{right:111px;top:17px;text-align:right}
.help small{display:block;font-size:12px;color:var(--muted)}
.help b{display:block;font-size:25px;color:var(--sky);margin-top:2px}
.nav{left:82px;top:88px;width:952px;height:36px;background:var(--crimson)}
.nav::before,.nav::after{content:"";position:absolute;bottom:-9px;border-top:9px solid var(--crimson-dark)}
.nav::before{left:0;border-left:12px solid transparent}
.nav::after{right:0;border-right:12px solid transparent}
.nav ul{list-style:none;display:flex;gap:26px;position:absolute;left:25px;top:9px}
.nav a{color:var(--white);text-decoration:none;font-weight:700;font-size:15px}
.social{position:absolute;right:27px;top:8px;display:flex;gap:5px}
.social span{width:20px;height:20px;border-radius:50%;background:var(--white)}
.video{left:108px;top:136px;width:624px;height:336px;background:#111}
.video .scene{position:absolute;left:0;top:0;width:624px;height:312px;background:linear-gradient(180deg,#1a1410 0%,#2b2018 55%,#6d5a46 80%,#8a7358 100%)}
.play{position:absolute;left:274px;top:119px;width:84px;height:84px;border-radius:50%;background:var(--crimson-dark)}
.play::after{content:"";position:absolute;left:32px;top:22px;border-left:30px solid var(--white);border-top:20px solid transparent;border-bottom:20px solid transparent}
.bar{position:absolute;left:0;bottom:0;width:624px;height:24px;background:#333}
.bar .btn{position:absolute;top:0;width:34px;height:24px;background:var(--sky)}
.bar .track{position:absolute;left:44px;top:8px;width:522px;height:8px;background:var(--white)}
.bar .track i{position:absolute;left:0;top:0;width:44px;height:8px;background:#999}
.optin{left:744px;top:136px;width:262px;height:336px;background:var(--sky);border:4px solid var(--sky-dark);text-align:center;color:var(--white)}
.optin h2{font-size:22px;line-height:27px;margin:16px 12px 0;font-weight:700}
.optin input{display:block;width:184px;height:34px;margin:0 auto 11px;border:0;border-radius:3px;padding:0 12px;font-family:inherit;font-size:12px;color:var(--muted)}
.optin .fields{margin-top:14px}
.optin button{width:184px;height:33px;border:0;border-radius:3px;background:var(--crimson);color:var(--white);font-family:inherit;font-weight:700;font-size:15px;margin-top:2px}
.optin p{font-size:12px;margin-top:14px}
.rule{left:108px;width:898px;border-top:3px dotted #d8d8d8}
.heading{left:106px;top:506px;width:900px;height:54px;background:linear-gradient(#fafafa,#ececec);text-align:center;font-size:28px;line-height:54px;color:var(--ink)}
.card{top:639px;width:216px;height:331px;background:linear-gradient(#f0f0f0,#fff 30%,#fff 75%,#eeeeee);box-shadow:inset 0 0 14px rgba(0,0,0,.08)}
.circle{top:580px;width:128px;height:128px;border-radius:50%;border:4px solid var(--white);box-shadow:0 1px 4px rgba(0,0,0,.2)}
.card h3{position:absolute;left:18px;top:94px;width:195px;font-size:15px;line-height:22px;color:var(--sky)}
.card p{position:absolute;left:18px;top:184px;width:190px;font-size:14px;line-height:22px;color:var(--body)}
.card a{position:absolute;left:18px;top:283px;width:94px;height:32px;background:var(--sky);color:var(--white);border-radius:3px;text-decoration:none;font-size:14px;line-height:32px;text-align:center}
.press{position:absolute;left:18px;top:94px;font-size:15px;font-weight:700;color:var(--sky)}
.media{position:absolute;left:0;width:216px;text-align:center;font-weight:700}
.logo-box{top:985px;width:170px;height:103px;background:linear-gradient(#f0f0f0,#fff 40%,#fff 70%,#ececec);box-shadow:inset 0 0 12px rgba(0,0,0,.08);text-align:center;line-height:103px;font-size:20px;font-weight:700;color:#a9a9a9}
.footer{left:0;width:1118px;text-align:center;font-size:12.5px;color:var(--ink)}
.footer a{color:var(--ink);text-decoration:none;margin:0 12px}
</style>
</head>
<body>
<div class="sheet"></div>

<header>
  <p class="abs tagline">Cracking The <strong>&ldquo;Secret Code&rdquo;</strong> That Unlocks<br>Your Wedding Cake Sales!</p>
  <div class="abs help"><small>We Can Help You, If You Have Any Questions</small><b>CALL US +821 555 0147</b></div>
</header>

<nav class="abs nav">
  <ul>
    <li><a href="#">HOME</a></li>
    <li><a href="#">WHO IS LEN VARGA</a></li>
    <li><a href="#">WHY LEN IS SHARING HIS SECRETS</a></li>
    <li><a href="#">CONTACT</a></li>
  </ul>
  <div class="social"><span></span><span></span><span></span></div>
</nav>

<section class="abs video">
  <div class="scene" role="img" aria-label="Video still of a ballroom with two draped booths"></div>
  <div class="play"></div>
  <div class="bar">
    <div class="btn" style="left:0"></div>
    <div class="track"><i></i></div>
    <div class="btn" style="right:0"></div>
  </div>
</section>

<aside class="abs optin">
  <h2>FREE Videos To Help You Sell More Wedding Cakes At Higher Prices&hellip; Immediately</h2>
  <div class="fields">
    <input type="text" placeholder="Your Name">
    <input type="email" placeholder="Email Address">
    <button>GET INSTANT ACCESS</button>
  </div>
  <p>No Spam. I Promise.</p>
</aside>

<div class="abs rule" style="top:498px"></div>
<h2 class="abs heading"><b>3 Leading-Edge</b> Techniques for Convincing Brides to Choose You</h2>
<div class="abs rule" style="top:564px"></div>

<article class="abs card" style="left:107px">
  <h3>In the first video, discover a sales growth secret that reveals the "Two Faces Of Your Wedding Cake Business."</h3>
  <p>One side of your face displays your "Internal Reality." It's how you run your business. Whether...</p>
  <a href="#">Read More</a>
</article>
<article class="abs card" style="left:335px">
  <h3>In the first video, discover a sales growth secret that reveals the "Two Faces Of Your Wedding Cake Business."</h3>
  <p>One side of your face displays your "Internal Reality." It's how you run your business. Whether...</p>
  <a href="#">Read More</a>
</article>
<article class="abs card" style="left:563px">
  <h3>In the first video, discover a sales growth secret that reveals the "Two Faces Of Your Wedding Cake Business."</h3>
  <p>One side of your face displays your "Internal Reality." It's how you run your business. Whether...</p>
  <a href="#">Read More</a>
</article>
<article class="abs card" style="left:792px">
  <span class="press">Len Varga as seen:</span>
  <span class="media" style="top:160px;font-size:30px;color:var(--ink)">Metro Wire</span>
  <span class="media" style="top:225px;font-size:30px;color:var(--crimson)">Daily Ledger</span>
</article>

<div class="abs circle" role="img" aria-label="Photo of a smiling woman pointing upward" style="left:151px;background:linear-gradient(#f4f4f4,#e6d6cc)"></div>
<div class="abs circle" role="img" aria-label="Photo of a woman giving two thumbs up" style="left:379px;background:linear-gradient(#f4f4f4,#6e6f86)"></div>
<div class="abs circle" role="img" aria-label="Photo of a tiered white wedding cake" style="left:607px;background:linear-gradient(#d8d8d8,#f4f2ec)"></div>
<div class="abs circle" style="left:836px;background:radial-gradient(circle,#1b4f8f,#0b2243);display:flex;align-items:center;justify-content:center;color:var(--white);font-size:17px;font-weight:700">Tri-City News</div>

<div class="abs logo-box" style="left:107px">Channel Nine</div>
<div class="abs logo-box" style="left:290px">Evening Post</div>
<div class="abs logo-box" style="left:473px">Signal</div>
<div class="abs logo-box" style="left:655px">Capital Herald</div>
<div class="abs logo-box" style="left:837px">Prime Review</div>

<footer>
  <p class="abs footer" style="top:1128px"><a href="#">Home</a>|<a href="#">Who Is Len Varga</a>|<a href="#">Why Len Is Sharing His Secrets</a>|<a href="#">Contact</a></p>
  <p class="abs footer" style="top:1155px">Copyright &copy; 2014 The Frosting Room. Phone: 402.555.0193. All Rights Reserved.</p>
</footer>
</body>
</html>
```